Report Design

I am looking for a redesign of our monthly inspection reports we submit to our customers. I uploaded the current one we use (FernHollow) and also that of a competitor (Calm Ridge). I want to more copy the layout of the Calmridge report I attached but with more flow and design.

Requirements
Must have
• This has to be in a template format that we can modify the content every month.

```html
<!DOCTYPE html>
<html lang="en">
<head>
<meta charset="utf-8">
<title>FernHollow Inspection Report</title>
<link href="https://fonts.googleapis.com/css2?family=Montserrat:wght@400;500;600;700&family=Roboto:ital,wght@1,700;1,900&display=swap" rel="stylesheet">
<style>
:root{
  --green:#0c9a36;
  --ink:#111;
  --canvas:#ebebeb;
  --band:#f1f1f1;
  --rule:#c9c9c9;
  --photo-green:#6f9a48;
  --photo-sky:#c9ced2;
}
*{box-sizing:border-box;margin:0;padding:0}
html,body{width:1200px;height:2647px;overflow:hidden}
body{background:var(--canvas);font-family:"Montserrat",sans-serif;color:var(--ink);position:relative}
.page{position:absolute;width:517px;height:731px;background:#fff;box-shadow:0 6px 18px rgba(0,0,0,.12);overflow:hidden}
.brand{font-family:"Montserrat",sans-serif;font-weight:700;color:var(--ink);display:flex;align-items:center;gap:6px}
.brand .dot{width:12px;height:12px;background:var(--green);border-radius:50%}
.title{position:absolute;left:0;right:0;text-align:center;font-family:"Roboto",sans-serif;font-style:italic;font-weight:900}
.title .l1{color:var(--green);font-size:38px;line-height:40px;display:block}
.title .l2{color:var(--ink);font-size:26px;line-height:30px;font-weight:700;display:block}
.rule{position:absolute;height:1px;background:var(--rule)}
.rule.centred::after{content:"";position:absolute;left:50%;top:-1px;width:32px;height:3px;margin-left:-16px;background:var(--green);border-radius:2px}
.subtitle{position:absolute;left:0;right:0;text-align:center;font-weight:600;font-size:14px}
.subtitle em{font-style:normal;color:var(--green)}
.band{position:absolute;left:0;right:0;background:var(--band)}
.photo{position:absolute;width:168px;height:115px;border:2px solid #fff;box-shadow:0 2px 6px rgba(0,0,0,.25);background:linear-gradient(180deg,var(--photo-sky) 0%,#d8dcdf 45%,var(--photo-green) 70%,#8b8f8c 100%)}
.item{position:absolute;width:205px}
.item .num{position:absolute;left:-40px;top:-6px;width:28px;height:28px;border-radius:50%;border:2px solid var(--green);border-left-color:#fff;background:#fff;color:var(--green);font-weight:700;font-size:14px;text-align:center;line-height:24px}
.item h3{font-size:12px;font-weight:600;margin-bottom:8px}
.item p{font-size:10.5px;line-height:12.5px}
.foot-url{position:absolute;right:36px;bottom:32px;height:18px;display:flex;align-items:center}
.foot-url span{background:var(--green);color:#fff;font-size:11px;font-weight:600;letter-spacing:.6px;padding:2px 10px 2px 16px;clip-path:polygon(8px 0,100% 0,100% 100%,0 100%)}
.foot-url b{width:22px;height:22px;border-radius:50%;border:2px solid var(--green);background:#fff;font-size:11px;text-align:center;line-height:18px;margin-left:-6px}
.foot-brand{position:absolute;left:32px;bottom:28px}
.foot-brand .brand{font-size:19px}
.foot-brand .tag{font-size:6.5px;font-weight:600;margin-top:3px}
</style>
</head>
<body>

<section class="page cover" style="left:55px;top:122px">
  <div style="position:absolute;left:28px;top:50px">
    <div class="brand" style="font-size:30px"><span class="dot"></span>FernHollow</div>
  </div>
  <svg width="517" height="500" viewBox="0 0 517 500" style="position:absolute;left:0;top:0">
    <defs>
      <linearGradient id="gardenTone" x1="0" y1="0" x2="0" y2="1">
        <stop offset="0" stop-color="#5e8f3c"/><stop offset=".55" stop-color="#4f7a34"/><stop offset="1" stop-color="#9a9a8c"/>
      </linearGradient>
      <linearGradient id="walkTone" x1="0" y1="0" x2="0" y2="1">
        <stop offset="0" stop-color="#cfd3d6"/><stop offset=".5" stop-color="#8c9a7e"/><stop offset="1" stop-color="#a5303a"/>
      </linearGradient>
    </defs>
    <polygon points="0,141 447,141 350,493 0,493" fill="url(#gardenTone)" role="img" aria-label="Photo of a landscaped garden with pond, shrubs and stone path"/>
    <polygon points="467,103 517,103 517,230 432,230" fill="var(--green)"/>
    <polygon points="425,240 517,240 517,493 355,493" fill="url(#walkTone)" role="img" aria-label="Photo of a sidewalk lined with red flower beds"/>
  </svg>
  <div class="title" style="top:518px;left:28px;text-align:left">
    <span class="l1" style="font-size:45px;line-height:46px">LANDSCAPE, IRR. &amp;</span>
    <span class="l2" style="font-size:30px;line-height:36px">PROPERTY INSPECTION</span>
  </div>
  <div class="rule" style="left:28px;top:607px;width:435px"></div>
  <div style="position:absolute;left:54px;top:606px;width:58px;height:4px;background:var(--green);border-radius:2px"></div>
  <div style="position:absolute;left:28px;top:626px;font-size:19px;font-weight:600">Gardens on Westmere <span style="color:var(--green)">POA &amp; Retail</span></div>
  <div style="position:absolute;left:30px;top:682px;font-size:14px;font-weight:600;letter-spacing:1px">www.fernhollow.com</div>
</section>

<section class="page" style="left:618px;top:122px">
  <div class="title" style="top:52px"><span class="l1">LANDSCAPE, IRR. &amp;</span><span class="l2">PROPERTY INSPECTION</span></div>
  <div class="rule centred" style="left:130px;width:257px;top:131px"></div>
  <div class="subtitle" style="top:148px">GARDENS ON WESTMERE <em>POA &amp; RETAIL</em></div>
  <div class="band" style="top:198px;height:294px"></div>
  <div style="position:absolute;left:180px;top:190px;width:157px;height:22px;background:var(--green);color:#fff;font-size:11px;font-weight:600;text-align:center;line-height:22px;border-radius:0 0 10px 10px">Month of November</div>
  <div class="photo" style="left:310px;top:232px" role="img" aria-label="Photo of a small tree among pink flowering grasses"></div>
  <div class="photo" style="left:310px;top:358px" role="img" aria-label="Photo of ornamental grasses along a building wall"></div>
  <div class="item" style="left:74px;top:307px"><span class="num">1</span><h3>Grasses Throughout</h3><p>Right now the Muhly grass is blooming and looks great. The crew went around and trimmed them all up so they look fresh and clean. There were some of the types that were not blooming, that we trimmed back farther.</p></div>
  <div class="photo" style="left:310px;top:514px" role="img" aria-label="Photo of a main entrance with empty flower bed"></div>
  <div class="item" style="left:74px;top:548px"><span class="num">2</span><h3>Flowers</h3><p>Both main entrances are in need of fresh flowers.</p></div>
  <div class="foot-brand"><div class="brand"><span class="dot"></span>FernHollow</div><div class="tag">Landscape and Maintenance, Inc.</div></div>
  <div class="foot-url"><span>www.fernhollow.com</span><b>1</b></div>
</section>

<section class="page" style="left:55px;top:941px">
  <div class="title" style="top:48px"><span class="l1">LANDSCAPE, IRR. &amp;</span><span class="l2">PROPERTY INSPECTION</span></div>
  <div class="rule centred" style="left:130px;width:257px;top:127px"></div>
  <div class="subtitle" style="top:140px;font-size:13px">Landscape and Grounds <em>Maintenance Division</em></div>
  <div class="band" style="top:182px;height:296px"></div>
  <div class="photo" style="left:36px;top:210px" role="img" aria-label="Photo of tall palm trees by a parking lot"></div>
  <div class="photo" style="left:36px;top:335px" role="img" aria-label="Photo of palms needing trimming"></div>
  <div class="item" style="left:273px;top:296px"><span class="num">3</span><h3>Palms Need Trimming</h3><p>All the Palms could use a trimming, there are dead frons and some hanging seed pods and boots. Let us know if and when you would like to get this scheduled.</p></div>
  <div class="photo" style="left:36px;top:500px" role="img" aria-label="Photo of a corner bed beside a road"></div>
  <div class="item" style="left:273px;top:536px"><span class="num">4</span><h3>Fill In</h3><p>We should fill this corner in where truck run over the corner with additional plants.</p></div>
  <div class="foot-brand"><div class="brand"><span class="dot"></span>FernHollow</div><div class="tag">Landscape and Maintenance, Inc.</div></div>
  <div class="foot-url"><span>www.fernhollow.com</span><b>2</b></div>
</section>

<section class="page" style="left:618px;top:941px">
  <div class="title" style="top:52px"><span class="l1">LANDSCAPE, IRR. &amp;</span><span class="l2">PROPERTY INSPECTION</span></div>
  <div class="rule centred" style="left:130px;width:257px;top:131px"></div>
  <div class="subtitle" style="top:149px;font-size:13px">Gardens on Westmere POA...cont</div>
  <div class="photo" style="left:311px;top:195px" role="img" aria-label="Photo of a tree bed next to parked cars"></div>
  <div class="item" style="left:80px;top:226px"><span class="num">5</span><h3>Fill in Coonties</h3><p>Coonties need to be filled in here. As well as side of Pine Grill.</p></div>
  <div class="band" style="top:330px;height:146px"></div>
  <div class="photo" style="left:37px;top:342px" role="img" aria-label="Photo of a washed out mulch bed by a wall"></div>
  <div class="item" style="left:274px;top:376px"><span class="num">6</span><h3>ulch:</h3><p>Overall the place could use fresh mulch, or we could just mulch these washed out areas that are an eye sore.</p></div>
  <div class="photo" style="left:311px;top:491px" role="img" aria-label="Photo of pruned small palms along a building"></div>
  <div class="item" style="left:80px;top:528px"><span class="num">7</span><h3>Pruning</h3><p>All the little palms have been pruned up to look clean</p></div>
  <div class="foot-brand"><div class="brand"><span class="dot"></span>FernHollow</div><div class="tag">Landscape and Maintenance, Inc.</div></div>
  <div class="foot-url"><span>www.fernhollow.com</span><b>3</b></div>
</section>

<section class="page back" style="left:341px;top:1768px">
  <div style="position:absolute;left:0;top:190px;width:517px;height:385px;background:linear-gradient(180deg,#fff 0%,#ececec 30%,#d9d9d9 60%,#e6e6e6 100%)" role="img" aria-label="Faded photo of a mountain valley with a lake"></div>
  <div style="position:absolute;left:0;right:0;top:518px;display:flex;flex-direction:column;align-items:center">
    <div class="brand" style="font-size:26px"><span class="dot"></span>FernHollow</div>
    <div style="font-size:9px;font-weight:600;margin-top:4px">Landscape and Maintenance, Inc.</div>
  </div>
  <div style="position:absolute;left:0;top:575px;width:517px;height:102px;background:var(--green);color:#fff;text-align:center;font-weight:600">
    <div style="font-size:8px;margin-top:22px">Landscape and Grounds Maintenance Division</div>
    <div style="font-size:9px;margin-top:10px">&#9742; 555-201-0100</div>
    <div style="font-size:9px;margin-top:5px">&#9742; 555-201-0199</div>
    <div style="font-size:7px;margin-top:6px">
      <svg width="8" height="10" viewBox="0 0 8 10" style="vertical-align:-1px"><path d="M4 0a4 4 0 0 0-4 4c0 3 4 6 4 6s4-3 4-6a4 4 0 0 0-4-4z" fill="#fff"/><circle cx="4" cy="4" r="1.5" fill="var(--green)"/></svg>
      1200 Orchard Lane Oak City, FL 30000</div>
  </div>
  <div style="position:absolute;left:0;right:0;top:688px;text-align:center;font-size:14px;font-weight:700;letter-spacing:1px">www.fernhollow.com</div>
</section>

</body>
</html>
```